House-share and Room Rental Website (With Focus on the Bedroom Landing Page)

Looking for website design for our House-share (executive accommodation) and room rental business.

Our company name is: Lodvenra could also be written as LodVenra or lodvenra. Either is fine .. just looking for a nice clean catchy logo to go with the design.

EXAMPLES
These are examples of other websites in this field that are doing well. this is a kind of baseline.
https://kelbrin.com.au/
https://www.tuvaplex.com/
https://www.nestorvi.com/
https://www.quillsa.net/
https://www.pendlebarrow.com.au/

Our business model is to rent rooms to people looking for high-quality accommodation. We fill the gap between those looking to rent rooms and those with rooms to rent. However, our model is slightly different from those already on the market as we looking to fill a massive gap in the market delivering upmarket rooms for rent.(Executive Accommodation) also in the back end will be coupled with a self management process in the back end.

We offer executive style accommodation that stands out above the rest. With special extras like fire safety.. and management processes that create happier homes. We are looking for a web design package that can help us grow and scale our business. We need a design that is captivating

Our MAIN focus is having a room landing page that stands out from the rest... The core of our business will rely on the promotion of the rooms in a share house... so the whole design relies on the BEDROOM landing page to drive results.

Target Market(s)

We have 2 markets we are aiming at ... the first market is people offering rooms to rent who want the highest rental return. The second market is people looking to rent safe, high-quality rooms, in houses that are well managed and looked after.

Industry/Entity Type

Share Economy

Logo Text

LodVenra

Number of Pages Required

5+ page

Font styles to use
Sans Serif

Colors
3276b5

Requirements
Must have
• A messaging system whereby we can create direct communication between those offering rooms and those looking for rooms.
• A call to action that says " Schedule an Inspection"
• Landing page for promoting rooms
• A home page for showing stock.
• Profile page for those selling rooms
• Profile page for those looking for rooms.
• A scheduling calendar for booking inspections
Nice to have
• Pages where new residents can lock in a room.. pay bond and rents.. and sign contracts
• Notifications
• SMS capabilities in the backend.
Should not have
• No script or handwriting fonts.

```html
<!DOCTYPE html>
<html lang="en">
<head>
<meta charset="utf-8">
<title>LodVenra – Bedroom</title>
<link href="https://fonts.googleapis.com/css2?family=Jost:wght@300;400;500&family=Playfair+Display:wght@900&family=Marcellus+SC&display=swap" rel="stylesheet">
<style>
:root{
  --brand:#3276b5;
  --brand-dark:#2a6aa8;
  --ink:#555a60;
  --ink-soft:#6b7075;
  --line:#e2e4e7;
  --white:#ffffff;
  --hero-dark:#2b2b2c;
  --chat-bg:#d9dadc;
}
*{box-sizing:border-box;margin:0;padding:0}
html,body{width:910px;height:1200px;overflow:hidden;background:var(--white)}
body{position:relative;font-family:"Jost",sans-serif;color:var(--ink)}
.abs{position:absolute}

.hero{left:0;top:0;width:910px;height:411px;
  background:radial-gradient(ellipse at 45% 60%,#9a9a9a 0%,#6c6c6c 35%,#3c3c3d 70%,var(--hero-dark) 100%)}
.brand{left:107px;top:50px;font-family:"Jost",sans-serif;font-weight:400;font-size:17px;letter-spacing:.5px;color:var(--white)}
.brand-dot{left:140px;top:14px;width:26px;height:26px;border-radius:50%;background:var(--brand)}

.top-btn{top:27px;height:27px;border:1px solid var(--brand);display:flex;align-items:center;color:var(--white);font-size:11.5px;font-weight:400;background:rgba(20,20,20,.35)}
.top-btn .ico{width:25px;height:100%;background:var(--brand);display:flex;align-items:center;justify-content:center;margin-right:9px}
.tour{left:512px;width:122px}
.signup{left:639px;width:84px}
.login{left:730px;width:72px}

.arrow{top:183px;width:45px;height:45px;border-radius:50%;border:3px solid rgba(255,255,255,.45);display:flex;align-items:center;justify-content:center}
.arrow-prev{left:29px}.arrow-next{left:837px}

.headline{left:0;width:910px;top:180px;text-align:center;font-family:"Playfair Display",serif;font-weight:900;font-size:33px;color:var(--white);letter-spacing:.5px}
.cta{left:378px;top:240px;width:155px;height:31px;border:1px solid var(--white);color:var(--white);font-size:10.5px;display:flex;align-items:center;justify-content:center;letter-spacing:.2px}

.strip{left:107px;top:355px;width:695px;height:99px;background:var(--white)}
.strip-shadow{left:140px;top:452px;width:630px;height:14px;border-radius:50%;background:radial-gradient(ellipse at center,rgba(0,0,0,.45) 0%,rgba(0,0,0,0) 70%)}
.thumb{top:364px;width:127px;height:82px}
.t1{left:118px;background:linear-gradient(160deg,#6b4a3a,#9c8c70 50%,#5a3a2c)}
.t2{left:254px;background:linear-gradient(160deg,#3d3a44,#8a6f58 50%,#4a3530)}
.t3{left:392px;background:linear-gradient(160deg,#d8d8d8,#9a9a9a 55%,#555)}
.t4{left:529px;background:linear-gradient(160deg,#4a3e36,#cfc9c2 55%,#8a7f74)}
.t5{left:666px;background:linear-gradient(160deg,#a9a6a3,#5b3b2e 55%,#2e221c)}

.tabs{left:107px;top:493px;width:695px;height:32px;border:1px solid var(--line);display:flex}
.tab{height:100%;display:flex;align-items:center;justify-content:center;font-family:"Marcellus SC",serif;font-size:12px;letter-spacing:.8px;color:var(--ink-soft);border-right:1px solid var(--line)}
.tab:last-child{border-right:none}
.tab.active{background:var(--brand);color:var(--white);box-shadow:0 3px 5px rgba(0,0,0,.25);height:34px;margin-top:-1px}

.intro{left:107px;top:563px;width:695px;text-align:center;font-size:10.5px;line-height:23.5px;color:var(--ink);font-weight:400}

.section-title{left:0;width:910px;top:673px;text-align:center;color:var(--brand);font-size:14px;font-weight:400}
.divider{left:405px;top:710px;width:100px;height:1px;background:linear-gradient(90deg,transparent,#c9cdd2,transparent)}
.divider-mark{left:449px;top:704px;width:12px;height:12px;border-radius:50%;background:var(--brand)}

.amenity{width:150px}
.amenity svg{display:block}
.amenity h3{font-weight:300;font-size:12.5px;color:var(--ink);margin:14px 0 14px}
.amenity ul{list-style:none}
.amenity li{font-size:9.6px;line-height:18.6px;color:var(--ink);display:flex;align-items:center;font-weight:400}
.amenity li svg{margin-right:5px;flex:none}
.col-rule{width:1px;background:var(--line)}
.row-rule{left:107px;top:919px;width:695px;height:1px;background:var(--line)}

.chat{left:696px;top:1126px;width:214px;height:34px;background:var(--chat-bg);display:flex;align-items:center}
.chat .chat-ico{width:26px;height:26px;background:var(--brand);margin-left:4px;display:flex;align-items:center;justify-content:center}
.chat span{margin-left:12px;font-size:14px;color:#5d6166;font-weight:300;flex:1}
.chat .plus{width:26px;height:26px;background:var(--brand);margin-right:4px;color:var(--white);font-size:18px;display:flex;align-items:center;justify-content:center}

.footer{left:0;top:1160px;width:910px;height:40px;background:var(--brand)}
.copy{left:106px;top:1172px;font-size:10px;color:var(--white);font-weight:400}
.social{top:1168px;width:21px;height:21px;border-radius:50%;border:1.5px solid var(--white);background:var(--brand-dark)}
</style>
</head>
<body>

<div class="abs hero" role="img" aria-label="Bright bedroom with a double bed, tall windows and an open ensuite with a freestanding bath"></div>
<div class="abs brand-dot"></div>
<div class="abs brand">LodVenra</div>

<div class="abs top-btn tour"><div class="ico"><svg width="13" height="13" viewBox="0 0 13 13" fill="none" stroke="#fff" stroke-width="1.2"><rect x="1" y="2" width="11" height="10"/><line x1="1" y1="5" x2="12" y2="5"/><line x1="4" y1="0.5" x2="4" y2="3"/><line x1="9" y1="0.5" x2="9" y2="3"/></svg></div>Schedule a Tour</div>
<div class="abs top-btn signup"><div class="ico"><svg width="13" height="13" viewBox="0 0 13 13" fill="#fff"><circle cx="6.5" cy="4" r="3"/><path d="M1 13c0-3.5 2.5-5.5 5.5-5.5S12 9.5 12 13z"/></svg></div>Sign Up</div>
<div class="abs top-btn login"><div class="ico"><svg width="13" height="13" viewBox="0 0 13 13" fill="#fff"><circle cx="6.5" cy="4" r="3"/><path d="M1 13c0-3.5 2.5-5.5 5.5-5.5S12 9.5 12 13z"/></svg></div>Log In</div>

<div class="abs arrow arrow-prev"><svg width="12" height="24" viewBox="0 0 12 24" fill="none" stroke="rgba(255,255,255,.7)" stroke-width="1.5"><path d="M10 2 2 12l8 10"/></svg></div>
<div class="abs arrow arrow-next"><svg width="12" height="24" viewBox="0 0 12 24" fill="none" stroke="rgba(255,255,255,.7)" stroke-width="1.5"><path d="M2 2l8 10-8 10"/></svg></div>

<h1 class="abs headline">NEED A PLACE FOR YOUR DREAM</h1>
<div class="abs cta">SCHEDULE AN INSPECTION</div>

<div class="abs strip-shadow"></div>
<div class="abs strip"></div>
<div class="abs thumb t1" role="img" aria-label="Lounge nook with a large window and city view"></div>
<div class="abs thumb t2" role="img" aria-label="Living room with armchairs and a work desk"></div>
<div class="abs thumb t3" role="img" aria-label="Bedroom with open ensuite"></div>
<div class="abs thumb t4" role="img" aria-label="Bathroom with bath and round mirror"></div>
<div class="abs thumb t5" role="img" aria-label="Hallway with timber door"></div>

<nav class="abs tabs">
  <div class="tab" style="width:183px">Description Bedroom</div>
  <div class="tab active" style="width:252px">Room Amenities (not Limited To)</div>
  <div class="tab" style="width:169px">Maps/What's Nearby</div>
  <div class="tab" style="width:91px">Reviews</div>
</nav>

<p class="abs intro">Lorem ipsum dolor sit amet, consectetuer adipiscing elit, sed diam nonummy nibh euismod tincidunt ut laoreet dolore magna aliquam erat volutpat. Ut wisi enim ad minim veniam, quis nostrud exerci tation ullamcorper suscipit lobortis nisl ut aliquip ex ea commodo consequat. Duis autem vel eum iriure dolor in hendrerit in vulputate velit esse molestie consequat, vel illum dolore eu feugiat nulla facilisis at vero eroset.</p>

<h2 class="abs section-title">THESE ARE SOME THINGS THAT MAY BE INCLUDED IN THE ROOM</h2>
<div class="abs divider"></div>
<div class="abs divider-mark"></div>

<div class="abs col-rule" style="left:281px;top:746px;height:142px"></div>
<div class="abs col-rule" style="left:454px;top:746px;height:142px"></div>
<div class="abs col-rule" style="left:628px;top:746px;height:142px"></div>
<div class="abs row-rule"></div>
<div class="abs col-rule" style="left:281px;top:944px;height:145px"></div>
<div class="abs col-rule" style="left:454px;top:944px;height:145px"></div>
<div class="abs col-rule" style="left:628px;top:944px;height:145px"></div>

<!-- row 1 -->
<div class="abs amenity" style="left:127px;top:746px">
  <svg width="40" height="40" viewBox="0 0 40 40" fill="none" stroke="#555" stroke-width="1.3"><rect x="1" y="1" width="14" height="11"/><circle cx="27" cy="7" r="4"/><rect x="4" y="20" width="22" height="10"/><rect x="1" y="26" width="28" height="8"/><rect x="31" y="14" width="6" height="22"/><line x1="34" y1="36" x2="34" y2="39"/></svg>
  <h3>Furnished</h3>
  <ul><li>Duis autem vel eum iriure dolor</li><li>Hendrerit in vulputate velit esse</li><li>Molestie consequat, vel illum</li><li>Dolore eu feugiat nulla facilisis</li></ul>
</div>
<div class="abs amenity" style="left:306px;top:746px">
  <svg width="40" height="40" viewBox="0 0 40 40" fill="none" stroke="#555" stroke-width="1.3"><rect x="1" y="1" width="37" height="38"/><rect x="4" y="4" width="16" height="32"/><rect x="22" y="4" width="13" height="10"/><rect x="22" y="15" width="13" height="10"/><rect x="22" y="26" width="13" height="10"/></svg>
  <h3>Storage space</h3>
  <ul><li><svg width="9" height="9" viewBox="0 0 10 10" fill="none" stroke="#3276b5" stroke-width="1.3"><circle cx="5" cy="5" r="4"/><path d="M3 5l1.5 1.5L8 2"/></svg>Duis autem vel eum 24x8</li><li><svg width="9" height="9" viewBox="0 0 10 10" fill="none" stroke="#3276b5" stroke-width="1.3"><circle cx="5" cy="5" r="4"/><path d="M3 5l1.5 1.5L8 2"/></svg>Hendrerit in vulputate 5x3</li><li><svg width="9" height="9" viewBox="0 0 10 10" fill="none" stroke="#3276b5" stroke-width="1.3"><circle cx="5" cy="5" r="4"/><path d="M3 5l1.5 1.5L8 2"/></svg>Molestie consequat, 2x2</li><li><svg width="9" height="9" viewBox="0 0 10 10" fill="none" stroke="#3276b5" stroke-width="1.3"><circle cx="5" cy="5" r="4"/><path d="M3 5l1.5 1.5L8 2"/></svg>Dolore eu feugiat 3x5</li></ul>
</div>
<div class="abs amenity" style="left:467px;top:746px">
  <svg width="40" height="40" viewBox="0 0 40 40" fill="none" stroke="#555" stroke-width="1.3"><rect x="14" y="1" width="18" height="12"/><line x1="23" y1="13" x2="23" y2="17"/><line x1="1" y1="18" x2="39" y2="18"/><rect x="1" y="18" width="14" height="18"/><line x1="36" y1="18" x2="36" y2="39"/><line x1="1" y1="27" x2="15" y2="27"/><rect x="2" y="6" width="3" height="12"/><rect x="6" y="8" width="3" height="10"/></svg>
  <h3>Study Desk / Workstation</h3>
  <ul><li><svg width="9" height="9" viewBox="0 0 10 10" fill="none" stroke="#3276b5" stroke-width="1.3"><circle cx="5" cy="5" r="4"/><path d="M3 5l1.5 1.5L8 2"/></svg>Duis autem vel eum iriure dolor</li><li><svg width="9" height="9" viewBox="0 0 10 10" fill="none" stroke="#3276b5" stroke-width="1.3"><circle cx="5" cy="5" r="4"/><path d="M3 5l1.5 1.5L8 2"/></svg>Hendrerit in vulputate velit esse</li><li><svg width="9" height="9" viewBox="0 0 10 10" fill="none" stroke="#3276b5" stroke-width="1.3"><circle cx="5" cy="5" r="4"/><path d="M3 5l1.5 1.5L8 2"/></svg>Molestie consequat, vel illum</li></ul>
</div>
<div class="abs amenity" style="left:653px;top:746px">
  <svg width="40" height="40" viewBox="0 0 40 40" fill="none" stroke="#555" stroke-width="1.3"><rect x="1" y="1" width="38" height="38"/><rect x="4" y="4" width="15" height="32"/><rect x="21" y="4" width="15" height="32"/><path d="M8 10h7l-1 5h-5z"/><rect x="7" y="16" width="9" height="12"/><line x1="24" y1="24" x2="33" y2="24"/></svg>
  <h3>Wardrobe</h3>
  <ul><li><svg width="9" height="9" viewBox="0 0 10 10" fill="none" stroke="#3276b5" stroke-width="1.3"><circle cx="5" cy="5" r="4"/><path d="M3 5l1.5 1.5L8 2"/></svg>Duis autem vel eum 24x8</li><li><svg width="9" height="9" viewBox="0 0 10 10" fill="none" stroke="#3276b5" stroke-width="1.3"><circle cx="5" cy="5" r="4"/><path d="M3 5l1.5 1.5L8 2"/></svg>Hendrerit in vulputate 5x3</li><li><svg width="9" height="9" viewBox="0 0 10 10" fill="none" stroke="#3276b5" stroke-width="1.3"><circle cx="5" cy="5" r="4"/><path d="M3 5l1.5 1.5L8 2"/></svg>Molestie consequat, 2x2</li></ul>
</div>

<!-- row 2 -->
<div class="abs amenity" style="left:127px;top:944px">
  <svg width="56" height="40" viewBox="0 0 56 40" fill="none" stroke="#555" stroke-width="1.3"><rect x="1" y="1" width="54" height="33"/><rect x="4" y="4" width="48" height="27"/><line x1="20" y1="38" x2="36" y2="38"/><line x1="28" y1="34" x2="28" y2="38"/></svg>
  <h3>TV</h3>
  <ul><li>Duis autem vel eum iriure dolor</li><li>Hendrerit in vulputate velit esse</li><li>Molestie consequat, vel illum</li><li>Dolore eu feugiat nulla facilisis</li></ul>
</div>
<div class="abs amenity" style="left:306px;top:944px">
  <svg width="40" height="40" viewBox="0 0 40 40" fill="none" stroke="#555" stroke-width="1.3"><path d="M2 22h34c0 9-6 13-17 13S2 31 2 22z"/><line x1="8" y1="35" x2="6" y2="39"/><line x1="30" y1="35" x2="32" y2="39"/><circle cx="10" cy="17" r="4"/><circle cx="17" cy="15" r="4"/><line x1="30" y1="22" x2="30" y2="8"/><rect x="27" y="3" width="6" height="5"/></svg>
  <h3>Ensuite shower</h3>
  <ul><li><svg width="9" height="9" viewBox="0 0 10 10" fill="none" stroke="#3276b5" stroke-width="1.3"><circle cx="5" cy="5" r="4"/><path d="M3 5l1.5 1.5L8 2"/></svg>Duis autem vel eum 24x8</li><li><svg width="9" height="9" viewBox="0 0 10 10" fill="none" stroke="#3276b5" stroke-width="1.3"><circle cx="5" cy="5" r="4"/><path d="M3 5l1.5 1.5L8 2"/></svg>Hendrerit in vulputate 5x3</li><li><svg width="9" height="9" viewBox="0 0 10 10" fill="none" stroke="#3276b5" stroke-width="1.3"><circle cx="5" cy="5" r="4"/><path d="M3 5l1.5 1.5L8 2"/></svg>Molestie consequat, 2x2</li><li><svg width="9" height="9" viewBox="0 0 10 10" fill="none" stroke="#3276b5" stroke-width="1.3"><circle cx="5" cy="5" r="4"/><path d="M3 5l1.5 1.5L8 2"/></svg>Dolore eu feugiat 3x5</li></ul>
</div>
<div class="abs amenity" style="left:465px;top:944px">
  <svg width="40" height="42" viewBox="0 0 40 42" fill="none" stroke="#555" stroke-width="1.3"><rect x="1" y="1" width="14" height="9"/><rect x="25" y="1" width="14" height="9"/><line x1="1" y1="22" x2="39" y2="22"/><rect x="1" y="22" width="38" height="18"/><rect x="4" y="26" width="12" height="11"/><line x1="22" y1="26" x2="22" y2="37"/><line x1="30" y1="26" x2="30" y2="37"/><line x1="5" y1="14" x2="5" y2="22"/><line x1="9" y1="14" x2="9" y2="22"/></svg>
  <h3 style="margin-top:14px">Kitchenette</h3>
  <ul><li><svg width="9" height="9" viewBox="0 0 10 10" fill="none" stroke="#3276b5" stroke-width="1.3"><circle cx="5" cy="5" r="4"/><path d="M3 5l1.5 1.5L8 2"/></svg>Duis autem vel eum iriure dolor</li><li><svg width="9" height="9" viewBox="0 0 10 10" fill="none" stroke="#3276b5" stroke-width="1.3"><circle cx="5" cy="5" r="4"/><path d="M3 5l1.5 1.5L8 2"/></svg>Hendrerit in vulputate velit esse</li><li><svg width="9" height="9" viewBox="0 0 10 10" fill="none" stroke="#3276b5" stroke-width="1.3"><circle cx="5" cy="5" r="4"/><path d="M3 5l1.5 1.5L8 2"/></svg>Molestie consequat, vel illum</li></ul>
</div>
<div class="abs amenity" style="left:652px;top:944px">
  <svg width="46" height="40" viewBox="0 0 46 40" fill="none" stroke="#555" stroke-width="1.3"><path d="M2 14 23 2l21 12v25H2z"/><path d="M7 39V17h32v22"/><path d="M12 30l3-7h16l3 7z"/><rect x="11" y="30" width="24" height="6"/><circle cx="15" cy="33" r="1.2"/><circle cx="31" cy="33" r="1.2"/></svg>
  <h3>Parking Area</h3>
  <ul><li><svg width="9" height="9" viewBox="0 0 10 10" fill="none" stroke="#3276b5" stroke-width="1.3"><circle cx="5" cy="5" r="4"/><path d="M3 5l1.5 1.5L8 2"/></svg>Duis autem vel eum 24x8</li><li><svg width="9" height="9" viewBox="0 0 10 10" fill="none" stroke="#3276b5" stroke-width="1.3"><circle cx="5" cy="5" r="4"/><path d="M3 5l1.5 1.5L8 2"/></svg>Hendrerit in vulputate 5x3</li><li><svg width="9" height="9" viewBox="0 0 10 10" fill="none" stroke="#3276b5" stroke-width="1.3"><circle cx="5" cy="5" r="4"/><path d="M3 5l1.5 1.5L8 2"/></svg>Molestie consequat, 2x2</li></ul>
</div>

<div class="abs chat">
  <div class="chat-ico"><svg width="14" height="14" viewBox="0 0 14 14" fill="none" stroke="#fff" stroke-width="1.2"><rect x="1" y="1" width="10" height="12"/><line x1="3" y1="5" x2="8" y2="5"/><line x1="3" y1="8" x2="7" y2="8"/><path d="M7 11l6-6"/></svg></div>
  <span>LIVE CHAT</span>
  <div class="plus">+</div>
</div>

<footer class="abs footer"></footer>
<div class="abs copy">Copyright © 2019 LodVenra. All Rights Reserved.</div>
<div class="abs social" style="left:703px"></div>
<div class="abs social" style="left:729px"></div>
<div class="abs social" style="left:755px"></div>
<div class="abs social" style="left:781px"></div>

</body>
</html>
```